Personal Injury Attorney Marketing Brochure to Medical Providers

We are looking to have a brochure - booklet form - outside - inside and back page - to hand out to chiropractors, physical therapist, clinics and other medical providers that treat persons who were injured - from an auto accident - truck accident - slip and fall, work related injury. We want them to know we handle personal injury work and represent persons who were injured as a result of the negligence of another person / company. We want the brochure to be professional and represent that we have a lot of experience in this area - Brian in practice since 1990 and Lena since 2000. Please refer to our website - www.fenwoodlegal.com for the type of work that we do and the practice areas. If we need to send more content - let us know. The project is to advertise only Brian Tolliver and lena Moskos.
Updates

We added a QR code to add to the brochure

Target Market(s)

Medical providers - such as chiropractors, Physical therapist, orthopedic doctors who may be able to refer a patient to a personal injury attorney who can help them pursue a personal injury claim

Industry/Entity Type

We are personal injury attorneys - we represent persons who have been injured in car accidents, trucking accidents, work site accidents, slip and falls that result in - broken bones, serious injuries and other injuries to help them get compensation

Font styles to use
Serif

Colors
0054AA
0677BA
7BADD7
CADEEF
E8F1F8

Requirements
Must have
• Photos of law firm members Brian Tolliver and Lena Moskos and our firm logo, our l numnew location address - which is 415 Wexbury Mill Rd., Norcross, GA 30071 / our direct phone numbers / e-mail address / website and information about us and our practice / Free consult / Attorney's who are very accessible / We have spanish speaking attorney and staff members. Please use only LEXRA or Google reviews for Brian Tolliver or Lena Moskos - not for Gordon Pellish. For e-mail contact to the firm - add admin@fenwoodlegal or admin3@fenwoodlegal.com - and add for Spanish - 404-555-0172 or for English - 404-555-0186
Nice to have
• Quotes from satisfied customers from Brian Tolliver and Lena Moskos's Google reviews and LEXRA reviews / our LEXRA ratings - all of which can be found on the internet - or we can provide - see attached word document with Google and LEXRA review information.
Should not have
• No guarantee of results

```html
<!DOCTYPE html>
<html lang="en">
<head>
<meta charset="utf-8">
<title>Fenwood Legal – Brochure Cover</title>
<link rel="stylesheet" href="https://fonts.googleapis.com/css2?family=Libre+Baskerville:wght@400;700&display=swap">
<style>
  :root {
    --canvas-bg: #d3d3d5;
    --paper: #f4f4f5;
    --ink: #2a2d3a;
    --ink-soft: #5a5d68;
    --brand-blue: #0677ba;
    --tile-navy: #34508a;
    --tile-deep: #2b4170;
    --tile-sky: #5ea2dc;
    --photo-a: #2f5ea8;
    --photo-b: #1f3f7a;
    --label: #ffffff;
  }
  * { box-sizing: border-box; margin: 0; padding: 0; }
  html, body { width: 1200px; height: 900px; overflow: hidden; }
  body {
    background: var(--canvas-bg);
    font-family: "Libre Baskerville", Georgia, serif;
    position: relative;
  }
  .cover {
    position: absolute;
    left: 283px; top: 40px;
    width: 634px; height: 820px;
    background: var(--paper);
    box-shadow: 0 18px 40px rgba(0,0,0,0.18);
    overflow: hidden;
  }
  .edge-band {
    position: absolute;
    left: 0; top: 272px;
    width: 9px; height: 548px;
    background: var(--brand-blue);
  }
  .firm-name {
    position: absolute;
    left: 40px; top: 254px;
    display: flex; align-items: center; gap: 10px;
    font-size: 14px; letter-spacing: 0.12em;
    color: var(--ink);
    text-transform: uppercase;
    white-space: nowrap;
  }
  .firm-name .mark {
    width: 14px; height: 14px;
    background: var(--brand-blue);
  }
  .headline {
    position: absolute;
    left: 40px; top: 288px;
    font-size: 23px; line-height: 1.05;
    letter-spacing: 0.1em;
    color: var(--ink);
    font-weight: 400;
  }
  .intro {
    position: absolute;
    left: 40px; top: 376px;
    width: 170px;
    font-size: 10px; line-height: 1.35;
    color: var(--ink-soft);
  }
  .tile {
    position: absolute;
    width: 76px; height: 62px;
  }
  .tile.navy { background: var(--tile-navy); }
  .tile.deep { background: var(--tile-deep); }
  .tile.sky  { background: var(--tile-sky); }
  .tile.photo {
    background: linear-gradient(135deg, var(--photo-a), var(--photo-b));
    display: flex; flex-direction: column;
    align-items: center; justify-content: center;
    color: var(--label);
    font-size: 10px; text-align: center; line-height: 1.2;
    padding: 4px;
  }
  .tile.photo.wide { width: 158px; font-size: 14px; }
  .tile .arrow { font-size: 12px; margin-top: 2px; }
</style>
</head>
<body>
  <main class="cover">
    <div class="edge-band"></div>

    <div class="firm-name"><span class="mark"></span>Fenwood Legal</div>

    <h1 class="headline">DRIVEN.<br>ATTENTIVE.<br>RELIABLE.</h1>

    <p class="intro">At Fenwood Legal, We See Ourselves As A Partner In Your Case, Rather Than Simply A Legal Expert.</p>

    <section class="practice-mosaic">
      <div class="tile photo" style="left:388px;top:40px" role="img" aria-label="Blue-toned photo of a car speedometer">car accidents<span class="arrow">→</span></div>
      <div class="tile navy" style="left:470px;top:40px"></div>

      <div class="tile navy" style="left:306px;top:108px"></div>
      <div class="tile photo" style="left:388px;top:108px" role="img" aria-label="Blue-toned photo of an elderly person's hands">nursing home abuse<span class="arrow">→</span></div>
      <div class="tile sky" style="left:470px;top:108px;width:158px;height:130px"></div>

      <div class="tile photo wide" style="left:224px;top:176px" role="img" aria-label="Blue-toned photo representing serious injuries">serious injuries<span class="arrow">→</span></div>
      <div class="tile navy" style="left:388px;top:176px"></div>

      <div class="tile photo" style="left:306px;top:244px" role="img" aria-label="Blue-toned photo of a rose">wrongful death<span class="arrow">→</span></div>
      <div class="tile sky" style="left:388px;top:244px"></div>
      <div class="tile navy" style="left:470px;top:244px"></div>

      <div class="tile deep" style="left:388px;top:312px"></div>
      <div class="tile photo" style="left:470px;top:312px" role="img" aria-label="Blue-toned photo of a wet floor">slip / fall injuries<span class="arrow">→</span></div>
      <div class="tile sky" style="left:552px;top:312px"></div>

      <div class="tile photo" style="left:552px;top:380px" role="img" aria-label="Blue-toned photo of a commercial truck">commercial truck accidents</div>
    </section>
  </main>
</body>
</html>
```